Tasman Curdworks Guild needs new business cards

We need new business cards designed and produced. We are likely to need other design work done for ads, flyers etc in future.

We would like to start with an initial business card.

The Tasman Curdworks Guild (TCG) is a membership-based not-for-profit organisation that looks after the interests of Australia's small to medium artisan cheesemakers, many of whom are also small-scale farmers. The design should be simple, using our logo, but also communicate our artisan cheese and small dairy farm focus.

The first card to be designed and produced is for me, Miriam Tolhurst. My details are:

Miriam Tolhurst
Secretary
Tasman Curdworks Guild (TCG)
http://www.curdworksguild.example
T +61452837190
E miriam.miriamtolhurst@mailbox.example

I have attached the TCG logo in jpg form. I have a higher resolution version available if needed.

Thank you!

Miriam

Miriam Tolhurst
Tasman Curdworks Guild
miriam.miriamtolhurst@mailbox.example
+61452837190

Sans Serif

• Logo (see attached file)

```html
<!DOCTYPE html>
<html lang="en">
<head>
<meta charset="utf-8">
<title>Tasman Curdworks Guild — Business Card</title>
<link rel="stylesheet" href="https://fonts.googleapis.com/css2?family=Arimo:wght@400;700&display=swap">
<style>
  :root {
    --stage: #000000;
    --card-white: #ffffff;
    --accent-orange: #f5a623;
    --text-brown: #5b2c0e;
    --cheese-yellow: #f9c74f;
    --gold-edge: #f8b638;
    --gold-mid: #fcd16a;
    --gold-light: #fde68f;
  }
  * { margin: 0; padding: 0; box-sizing: border-box; }
  html, body {
    width: 1200px; height: 900px; overflow: hidden;
    background: var(--stage);
    font-family: "Arimo", Arial, sans-serif;
  }
  .stage { position: relative; width: 1200px; height: 900px; }
  .card {
    position: absolute; top: 271px;
    width: 458px; height: 281px; border-radius: 13px; overflow: hidden;
  }
  .card--front { left: 137px; background: var(--card-white); }
  .card--back {
    left: 626px;
    background: linear-gradient(90deg, var(--gold-edge) 0%, var(--gold-mid) 22%, var(--gold-light) 45%, var(--gold-mid) 75%, var(--gold-edge) 100%);
  }
  .holder-name {
    position: absolute; left: 27px; top: 27px;
    font-size: 22px; font-weight: 700; color: var(--accent-orange); letter-spacing: 0.2px;
  }
  .holder-role {
    position: absolute; left: 27px; top: 52px;
    font-size: 16px; color: var(--text-brown);
  }
  .guild-mark { position: absolute; display: flex; align-items: center; }
  .guild-mark__dot { border-radius: 50%; background: var(--cheese-yellow); flex: none; }
  .guild-mark__name { color: var(--text-brown); font-weight: 400; line-height: 1.2; }
  .card--front .guild-mark { left: 236px; top: 30px; }
  .card--front .guild-mark__dot { width: 44px; height: 44px; margin-right: 14px; }
  .card--front .guild-mark__name { font-size: 16px; }
  .card--back .guild-mark { left: 78px; top: 90px; }
  .card--back .guild-mark__dot { width: 84px; height: 84px; margin-right: 30px; background: var(--card-white); }
  .card--back .guild-mark__name { font-size: 25px; line-height: 1.22; }
  .contact-list {
    position: absolute; left: 28px; top: 199px; list-style: none;
  }
  .contact-list li {
    display: flex; align-items: center; height: 19px;
    font-size: 13px; color: var(--text-brown);
  }
  .contact-list svg { width: 11px; height: 11px; margin-right: 8px; fill: var(--accent-orange); }
</style>
</head>
<body>
<main class="stage">
  <section class="card card--front">
    <h1 class="holder-name">Miriam Tolhurst</h1>
    <p class="holder-role">Secretary</p>
    <div class="guild-mark">
      <span class="guild-mark__dot"></span>
      <span class="guild-mark__name">Tasman<br>Curdworks<br>Guild</span>
    </div>
    <ul class="contact-list">
      <li>
        <svg viewBox="0 0 12 12" aria-hidden="true"><path d="M1 4c0-2 2-3 5-3s5 1 5 3v1H8V4H4v1H1z M3 6h6l1.5 5h-9z"/></svg>
        +61452837190
      </li>
      <li>
        <svg viewBox="0 0 12 12" aria-hidden="true"><rect x="0.5" y="2" width="11" height="8"/><path d="M0.5 2L6 6.5L11.5 2" stroke="#fff" stroke-width="1" fill="none"/></svg>
        miriam.miriamtolhurst@mailbox.example
      </li>
      <li>
        <svg viewBox="0 0 12 12" aria-hidden="true"><circle cx="6" cy="6" r="5.5"/><path d="M3 4c1 0 2 1 1.5 2S6 8 5 10M8 2.5c-1 1 0 2 1.5 2" stroke="#fff" stroke-width="1" fill="none"/></svg>
        www.curdworksguild.example
      </li>
    </ul>
  </section>

  <section class="card card--back">
    <div class="guild-mark">
      <span class="guild-mark__dot"></span>
      <span class="guild-mark__name">Tasman<br>Curdworks<br>Guild</span>
    </div>
  </section>
</main>
</body>
</html>
```